Website Design - KeyStagingHelpers.com

PLEASE CHECK WORD DOCUMENT ATTACHED FOR WEBSITE FLOW.

Target Market(s)

REAL ESTATE AGENTS ARE THE TARGET MARKET

Industry/Entity Type

Real Estate

Coding

Coded - Design and coding required

Number of Pages Required

4 page

Colors

Designer to choose colors to be used in the design.

Requirements
Must have
• WE LIKE RED LOGO ATTACHED
Nice to have
• PLEASE CHECK WORD DOCUMENT ATTACHED FOR WEBSITE FLOW.
Should not have

```html
<!DOCTYPE html>
<html lang="en">
<head>
<meta charset="utf-8">
<title>Key Staging Helpers</title>
<link href="https://fonts.googleapis.com/css2?family=Lato:wght@400;700&display=swap" rel="stylesheet">
<style>
:root{
  --navy:#2d2f8f;
  --ink:#222;
  --header-bg:#f6f7f9;
  --lavender:#b3b8f0;
  --card-blue:#0054a6;
  --card-border:#7a6ff0;
  --btn-blue:#0a0cbf;
  --pink:#ec1563;
  --footer:#383838;
  --white:#fff;
  --red:#e3202a;
  --social:#0a66b0;
}
*{margin:0;padding:0;box-sizing:border-box}
html,body{width:1200px;height:1200px;overflow:hidden}
body{font-family:'Lato',sans-serif;color:var(--ink);position:relative;background:var(--white)}
.site-header{position:absolute;top:0;left:0;width:1200px;height:81px;background:var(--header-bg)}
.brand{position:absolute;left:148px;top:22px;display:flex;align-items:center;gap:8px}
.brand-mark{width:26px;height:26px;border:4px solid var(--navy)}
.brand-name{font-weight:700;font-size:19px;color:var(--navy);line-height:1}
.main-nav{position:absolute;left:360px;top:26px;display:flex;align-items:center;font-size:15.5px}
.main-nav a{color:var(--ink);text-decoration:none;margin-right:18px}
.main-nav a.active{background:var(--navy);color:var(--white);padding:5px 6px;margin-right:17px}
.phone{position:absolute;left:921px;top:29px;display:flex;align-items:center;gap:6px;font-size:15.5px}
.hero{position:absolute;top:81px;left:0;width:1200px;height:552px;
  background:linear-gradient(180deg,#5d92d8 0%,#8ab7e6 22%,#5a8b45 55%,#3f7a2e 75%,#8c9aa3 90%,#7d8e84 100%)}
.hero-text{position:absolute;left:161px;top:428px;color:var(--white);font-weight:700;font-size:19.5px;line-height:30px;text-shadow:0 1px 3px rgba(0,0,0,.5)}
.offers{position:absolute;top:633px;left:0;width:1200px;height:344px;background:var(--lavender)}
.offer-card{position:absolute;top:30px;width:247px;height:147px;background:var(--card-blue);border:5px solid var(--card-border);border-radius:3px;text-align:center;color:var(--white)}
.offer-card p{font-weight:700;font-size:12.5px;margin-top:59px}
.offer-card a{display:block;width:128px;height:36px;margin:18px auto 0;background:var(--btn-blue);color:var(--white);border-radius:5px;font-weight:700;font-size:13px;line-height:36px;text-decoration:none}
.sign-pack{position:absolute;top:229px;width:129px;height:49px;background:var(--pink);color:var(--white);font-weight:700;font-size:15.5px;text-align:center;line-height:49px;text-decoration:none}
.site-footer{position:absolute;top:977px;left:0;width:1200px;height:223px;background:var(--footer);color:var(--white)}
.quick-links{position:absolute;left:150px;top:32px}
.quick-links h3,.footer-about h3{font-size:16px;font-weight:700}
.quick-links ul{list-style:none;margin-top:8px}
.quick-links li{font-size:14px;line-height:19px;margin-left:2px}
.footer-brand{position:absolute;left:449px;top:40px;display:flex;align-items:center;gap:8px}
.footer-brand .brand-mark{border-color:var(--red);background:var(--red)}
.footer-brand .brand-name{color:var(--red);font-size:17px}
.footer-about{position:absolute;left:646px;top:32px;width:370px}
.footer-about p{font-size:14.5px;line-height:14.5px;margin-top:2px}
.social{position:absolute;left:872px;top:181px;display:flex;gap:11px}
.social span{width:35px;height:35px;border-radius:50%;background:var(--social);display:block}
</style>
</head>
<body>
<header class="site-header">
  <div class="brand"><span class="brand-mark"></span><span class="brand-name">Key Staging Helpers</span></div>
  <nav class="main-nav">
    <a class="active" href="#">HOW IT WORKS</a>
    <a href="#">SERVICE AREA</a>
    <a href="#">PRICING</a>
    <a href="#">ABOUT US</a>
    <a href="#">FAQ</a>
  </nav>
  <div class="phone">
    <svg width="20" height="20" viewBox="0 0 24 24"><path fill="#222" d="M6.6 10.8a15 15 0 0 0 6.6 6.6l2.2-2.2c.3-.3.7-.4 1-.2 1.1.4 2.3.6 3.6.6.6 0 1 .4 1 1V20c0 .6-.4 1-1 1A17 17 0 0 1 3 4c0-.6.4-1 1-1h3.5c.6 0 1 .4 1 1 0 1.3.2 2.5.6 3.6.1.3 0 .7-.2 1z"/></svg>
    <span>077-5550190</span>
  </div>
</header>

<section class="hero" role="img" aria-label="Photo of a single-storey cream house with red shutters, green lawn, trees and blue sky">
  <div class="hero-text">
    <p>Helping agents save time and money.</p>
    <p>We place signs and boost foot traffic to your open houses using proven marketing techniques.</p>
  </div>
</section>

<section class="offers">
  <div class="offer-card" style="left:149px"><p>I'M A FULL ON BROKERAGE</p><a href="#">GET NOW</a></div>
  <div class="offer-card" style="left:473px"><p>I'M &nbsp;AN IND. BROKER WITH A TEAM</p><a href="#">GET NOW</a></div>
  <div class="offer-card" style="left:803px"><p>I NEED SIGN PLACEMENT ASAP</p><a href="#">BUY NOW</a></div>
  <a class="sign-pack" href="#" style="left:151px">5 SIGNS</a>
  <a class="sign-pack" href="#" style="left:348px;top:231px">10 SIGNS</a>
  <a class="sign-pack" href="#" style="left:536px;top:230px">15 SIGNS</a>
  <a class="sign-pack" href="#" style="left:734px;top:232px">20 SIGNS</a>
  <a class="sign-pack" href="#" style="left:915px">25 SIGNS</a>
</section>

<footer class="site-footer">
  <div class="quick-links">
    <h3>QUICK LINKS</h3>
    <ul><li>HOW IT WORKS</li><li>SERVICE AREA</li><li>PRICING</li><li>ABOUT US</li><li>FAQ</li></ul>
  </div>
  <div class="footer-brand"><span class="brand-mark"></span><span class="brand-name">Key Staging Helpers</span></div>
  <div class="footer-about">
    <h3>ABOUT</h3>
    <p>Lorem Ipsum is simply dummy text of the printing text and typesetting industry. Lorem Ipsum has been the industry's standard dummy text ever since the &nbsp;of the 1500s, when an unknown printer took a galley of a tex type and scrambled it to make a type specimen book. It has survived not only five centuries, but also the leap into electronic typesetting, remaining essenti unchange.</p>
  </div>
  <div class="social" aria-label="Social links"><span></span><span></span><span></span><span></span></div>
</footer>
</body>
</html>
```